brindlewood carpentry business card 2.0

id like to get some extra info added to my current business card ,but i am also open to a new design as well ,id like it to be a clean professional look
i have attached the original card files, i have also attached the ridgemark guild logo and licensed builder logo that id like to add to all the current info on the old card
also the color green is important as seen in the company logo

Industry/Entity Type

Carpentry

Colors
9bcb3c

```html
<!DOCTYPE html>
<html lang="en">
<head>
<meta charset="utf-8">
<title>Brindlewood Carpentry – Business Cards</title>
<link rel="stylesheet" href="https://fonts.googleapis.com/css2?family=Montserrat:wght@500&family=Poppins:wght@400;500;600&display=swap">
<style>
  :root {
    --green: #9bcb3c;
    --charcoal: #3b3b3c;
    --ink: #2a2a2a;
    --paper: #ffffff;
    --backdrop: #1e1e20;
    --muted: #444;
  }
  * { box-sizing: border-box; margin: 0; padding: 0; }
  html, body { width: 1200px; height: 874px; overflow: hidden; }
  body {
    background: var(--backdrop);
    font-family: "Poppins", sans-serif;
    position: relative;
  }
  .card {
    position: absolute;
    top: 283px;
    width: 540px;
    height: 308px;
    border-radius: 18px;
    overflow: hidden;
  }

  /* Brand side */
  .card--brand { left: 40px; background: var(--charcoal); }
  .brand-name {
    position: absolute;
    top: 70px;
    left: 0; right: 0;
    text-align: center;
    font-family: "Montserrat", sans-serif;
    font-weight: 500;
    color: var(--paper);
    line-height: 1.1;
  }
  .brand-name__main { display: block; font-size: 44px; letter-spacing: 2px; }
  .brand-name__sub { display: block; font-size: 26px; letter-spacing: 3px; margin-top: 6px; }
  .brand-band {
    position: absolute;
    left: 0; right: 0;
    top: 218px;
    height: 46px;
    background: var(--green);
    display: flex;
    align-items: center;
    justify-content: center;
  }
  .brand-band__url {
    font-family: "Poppins", sans-serif;
    font-weight: 500;
    font-size: 13px;
    letter-spacing: 5px;
    color: var(--ink);
    text-transform: uppercase;
  }
  .badge {
    position: absolute;
    top: 222px;
  }
  .badge--round {
    left: 16px;
    width: 38px; height: 38px;
    border-radius: 50%;
    background: var(--charcoal);
    border: 2px solid var(--paper);
  }
  .badge--square {
    right: 18px;
    width: 34px; height: 38px;
    background: #1d3b8c;
  }

  /* Contact side */
  .card--contact { left: 620px; background: var(--paper); }
  .contact-panel {
    position: absolute;
    top: 0; right: 0;
    width: 150px; height: 100%;
    background: var(--charcoal);
  }
  .contact-panel__stripe {
    position: absolute;
    top: 0; bottom: 0; left: 0;
    width: 14px;
    background: var(--green);
    border-right: 8px solid var(--paper);
  }
  .contact {
    position: absolute;
    left: 40px;
    top: 112px;
    color: var(--ink);
  }
  .contact__name {
    font-weight: 600;
    font-size: 26px;
    color: var(--green);
    letter-spacing: 0.5px;
    line-height: 1;
  }
  .contact__role { font-size: 14px; margin-top: 2px; }
  .contact__company { font-size: 15px; color: var(--muted); margin-top: 14px; }
  .contact__list { list-style: none; margin-top: 8px; font-size: 14px; color: var(--muted); }
  .contact__list li { display: flex; align-items: center; gap: 8px; line-height: 1.4; }
  .contact__list svg { width: 12px; height: 12px; flex: none; }
</style>
</head>
<body>

<section class="card card--brand">
  <h1 class="brand-name">
    <span class="brand-name__main">BRINDLEWOOD</span>
    <span class="brand-name__sub">CARPENTRY</span>
  </h1>
  <div class="brand-band">
    <span class="brand-band__url">www.brindlewoodcarpentry.co.nz</span>
  </div>
  <div class="badge badge--round" aria-label="Licensed builder badge"></div>
  <div class="badge badge--square" aria-label="Ridgemark Guild badge"></div>
</section>

<section class="card card--contact">
  <div class="contact-panel"><div class="contact-panel__stripe"></div></div>
  <div class="contact">
    <h2 class="contact__name">DANIEL HARKER</h2>
    <p class="contact__role">Director</p>
    <p class="contact__company">Brindlewood Carpentry Ltd</p>
    <ul class="contact__list">
      <li>
        <svg viewBox="0 0 12 12"><path fill="#9bcb3c" d="M2.5 0.5l2 2-1 1.5c.6 1.5 1.8 2.7 3.5 3.5l1.5-1 2 2-1 2C5 10.5 1.5 7 .5 2.5z"/></svg>
        02109845671
      </li>
      <li>
        <svg viewBox="0 0 12 12"><rect x="0.5" y="2" width="11" height="8" fill="#9bcb3c"/><path d="M0.5 2l5.5 4.5L11.5 2" fill="none" stroke="#fff" stroke-width="1"/></svg>
        dan@brindlewoodcarpentry.co.nz
      </li>
      <li>
        <svg viewBox="0 0 12 12"><circle cx="6" cy="6" r="5.5" fill="#9bcb3c"/><path d="M0.5 6h11M6 .5c-2.5 3-2.5 8 0 11M6 .5c2.5 3 2.5 8 0 11" fill="none" stroke="#fff" stroke-width="0.8"/></svg>
        brindlewoodcarpentry.co.nz
      </li>
    </ul>
  </div>
</section>

</body>
</html>
```